Business cards for property management company

Need new business cards designed for our property management company and rental community, Blue Fern Commons. These cards will be primarily picked up by rental applicants.

May be single or double sided design.

I need cards for two different people, listed below. The design can be the same for both, and the only information that will be different is name and email address.

Industry/Entity Type

Property Management

Requirements
Must have
• US standard business card - 2''x3.5'' horizontal design.

1. Logo (attached). The text does not have to stay below the logo, but the card does need to say "Blue Fern Commons" somewhere on it (does not have to be same font as logo, but those fonts are Americana Extra Bold and BlackJack if needed).
2. Name: one with "Paula Whitcombe" and one with "Darrell Whitcombe"
3. Email address: one with "paula@bluefernhome.com" and one with "darrell@bluefernhome.com"
4. Web address: bluefernhome.com
5. Phone: 281.604.2218
6. Address: 1783 Wexford Lane, Porterfield, Texas 77812 (zip code may me omitted, at your discretion)
Should not have
• No rounded corners or special cuts.

No bevel, emboss or shadow effects.

As a note, please do not use our website as a basis for color or design schemes. We are working on a redesign, based around the new logo (attached to brief).

```html
<!DOCTYPE html>
<html lang="en">
<head>
<meta charset="utf-8">
<title>Blue Fern Commons — Business Cards</title>
<link href="https://fonts.googleapis.com/css2?family=Didact+Gothic&family=Nunito+Sans:wght@700&display=swap" rel="stylesheet">
<style>
  :root {
    --backdrop: #d9dadb;
    --fern-green: #3b8d37;
    --card-white: #f7f8f7;
    --ink: #2a2a2a;
    --teal: #1d8fb3;
    --mark-faint: #e6ebe6;
  }
  html, body {
    margin: 0;
    padding: 0;
    overflow: hidden;
  }
  .canvas {
    position: relative;
    width: 1200px;
    height: 900px;
    background: var(--backdrop);
    overflow: hidden;
    font-family: "Didact Gothic", sans-serif;
  }
  .card {
    position: absolute;
    width: 560px;
    height: 320px;
    box-sizing: border-box;
    overflow: hidden;
  }

  /* Front */
  .card-front {
    left: 110px;
    top: 90px;
    background: var(--fern-green);
    color: #ffffff;
  }
  .front-brand {
    position: absolute;
    left: 0;
    right: 0;
    top: 112px;
    display: flex;
    align-items: center;
    justify-content: center;
    gap: 16px;
  }
  .brand-dot {
    width: 54px;
    height: 54px;
    border-radius: 50%;
    flex: none;
  }
  .card-front .brand-dot { border: 3px solid #ffffff; box-sizing: border-box; }
  .brand-name {
    font-size: 30px;
    letter-spacing: 0.5px;
    line-height: 1;
  }
  .front-web {
    position: absolute;
    left: 0;
    right: 0;
    bottom: 38px;
    text-align: center;
    font-size: 15px;
    letter-spacing: 0.6px;
  }

  /* Back */
  .card-back {
    left: 530px;
    top: 500px;
    background: var(--card-white);
    color: var(--ink);
  }
  .back-mark {
    position: absolute;
    right: -60px;
    top: 40px;
    width: 260px;
    height: 260px;
    border-radius: 50%;
    background: var(--mark-faint);
    opacity: 0.7;
  }
  .back-person {
    position: absolute;
    right: 34px;
    top: 34px;
    text-align: right;
  }
  .person-name {
    font-family: "Nunito Sans", sans-serif;
    font-weight: 700;
    font-size: 19px;
    color: var(--teal);
    letter-spacing: 0.3px;
  }
  .person-email {
    font-size: 13px;
    margin-top: 2px;
  }
  .back-brand {
    position: absolute;
    left: 30px;
    top: 168px;
    display: flex;
    align-items: center;
    gap: 12px;
    color: var(--fern-green);
  }
  .card-back .brand-dot { background: var(--fern-green); width: 40px; height: 40px; }
  .card-back .brand-name { font-size: 24px; }
  .back-contact {
    position: absolute;
    left: 30px;
    top: 240px;
    font-size: 14px;
    line-height: 1.5;
  }
  .phone-list {
    display: flex;
    gap: 14px;
  }
  .phone-item {
    display: inline-flex;
    align-items: center;
    gap: 5px;
  }
  .phone-icon {
    width: 13px;
    height: 13px;
    fill: var(--fern-green);
  }
</style>
</head>
<body>
<main class="canvas">

  <section class="card card-front" aria-label="Card front">
    <div class="front-brand">
      <span class="brand-dot"></span>
      <span class="brand-name">Blue Fern Commons</span>
    </div>
    <div class="front-web">www.bluefernhome.com</div>
  </section>

  <section class="card card-back" aria-label="Card back">
    <div class="back-mark" aria-hidden="true"></div>
    <div class="back-person">
      <div class="person-name">Paula Whitcombe</div>
      <div class="person-email">paula@bluefernhome.com</div>
    </div>
    <div class="back-brand">
      <span class="brand-dot"></span>
      <span class="brand-name">Blue Fern Commons</span>
    </div>
    <div class="back-contact">
      <div class="address">1783 Wexford Lane, Porterfield, Texas 77812</div>
      <div class="phone-list">
        <span class="phone-item">
          <svg class="phone-icon" viewBox="0 0 24 24" aria-hidden="true"><path d="M6.6 10.8a15.1 15.1 0 0 0 6.6 6.6l2.2-2.2a1 1 0 0 1 1-.25 11.4 11.4 0 0 0 3.6.57 1 1 0 0 1 1 1V20a1 1 0 0 1-1 1A17 17 0 0 1 3 4a1 1 0 0 1 1-1h3.5a1 1 0 0 1 1 1c0 1.25.2 2.45.57 3.57a1 1 0 0 1-.25 1z"/></svg>
          281.604.2218
        </span>
        <span class="phone-item">
          <svg class="phone-icon" viewBox="0 0 24 24" aria-hidden="true"><path d="M6.6 10.8a15.1 15.1 0 0 0 6.6 6.6l2.2-2.2a1 1 0 0 1 1-.25 11.4 11.4 0 0 0 3.6.57 1 1 0 0 1 1 1V20a1 1 0 0 1-1 1A17 17 0 0 1 3 4a1 1 0 0 1 1-1h3.5a1 1 0 0 1 1 1c0 1.25.2 2.45.57 3.57a1 1 0 0 1-.25 1z"/></svg>
          281.604.5597
        </span>
      </div>
    </div>
  </section>

</main>
</body>
</html>
```